Talvero Engineering & Management Services Website

A professional website design that outlines Engineering and Management Services. The website is to be colour coordinated with the current logo (see attached). The webpage needs to be compatible with Wordpress to allow for easy changes to be made to the website for the user.
Required tabs for the page include:
- Civil Engineering
- Structural Engineering
- Project Management
- Business Management
- Project Controls
- Drafting
- Contact Us

Clean and efficient website that matches the services provided by the business.

Target Market(s)

New Customers to a very competitive market

Industry/Entity Type

Engineering

Number of Pages Required

5+ page

Requirements
Must have
• Clean with large stock photos

```html
<!DOCTYPE html>
<html lang="en">
<head>
<meta charset="utf-8">
<title>Talvero Engineering &amp; Management Services</title>
<link rel="stylesheet" href="https://fonts.googleapis.com/css2?family=Open+Sans:wght@400;600;700&family=Roboto:wght@400;500;700&display=swap">
<style>
:root{
  --orange:#f15a22;
  --orange-dark:#d94a16;
  --ink:#333333;
  --muted:#777777;
  --light:#f4f4f4;
  --navy:#2a2f36;
  --charcoal:#1f2226;
  --white:#ffffff;
  --line:#dddddd;
}
*{margin:0;padding:0;box-sizing:border-box}
html,body{width:1200px;height:2204px;overflow:hidden}
body{font-family:"Open Sans",Arial,sans-serif;color:var(--ink);background:var(--white);position:relative}
section,header,footer{position:absolute;left:0;width:1200px}
.wrap{position:relative;width:1060px;margin:0 auto;height:100%}

/* header + hero */
.hero{top:0;height:492px;background:linear-gradient(160deg,#7d8a96 0%,#5b6772 40%,#3e4852 100%)}
.hero-photo{position:absolute;inset:0;background:linear-gradient(180deg,rgba(150,165,178,.55),rgba(40,48,56,.75))}
.topbar{position:absolute;top:0;left:0;width:1200px;height:52px;background:rgba(20,24,28,.75)}
.brand{position:absolute;left:70px;top:9px;display:flex;align-items:center;gap:10px;background:var(--white);padding:4px 14px 4px 6px;height:36px}
.brand-dot{width:26px;height:26px;border-radius:50%;background:var(--orange)}
.brand-name{font-family:"Roboto",sans-serif;font-weight:700;font-size:15px;color:var(--charcoal);letter-spacing:.5px}
.nav{position:absolute;right:70px;top:0;height:52px;display:flex;align-items:center;gap:26px;font-size:14px;color:var(--white)}
.nav .phone{background:var(--orange);padding:6px 12px;font-weight:700}
.hero-text{position:absolute;top:346px;left:0;width:1200px;text-align:center;color:var(--white);font-weight:700;font-size:20px;line-height:30px}
.btn{display:inline-block;background:var(--orange);color:var(--white);font-weight:700;font-size:15px;padding:12px 28px;text-transform:uppercase}
.hero-cta{position:absolute;top:420px;left:0;width:1200px;text-align:center}
.slide-arrow{position:absolute;top:240px;width:26px;height:34px;background:rgba(0,0,0,.55)}
.slide-arrow.left{left:0}.slide-arrow.right{right:0}

/* services */
.services{top:492px;height:436px;background:var(--white);text-align:center}
.sec-title{font-family:"Roboto",sans-serif;font-size:32px;font-weight:400;letter-spacing:1px;color:var(--charcoal)}
.sec-title b{color:var(--orange);font-weight:500}
.services .sec-title{padding-top:62px}
.sec-sub{font-size:14px;color:var(--muted);margin-top:8px}
.service-grid{display:flex;justify-content:space-between;margin-top:50px}
.service{width:160px}
.service .ring{width:80px;height:80px;border:3px solid var(--orange);border-radius:50%;margin:0 auto;display:flex;align-items:center;justify-content:center}
.service h3{font-size:15px;font-weight:600;margin-top:16px;color:var(--charcoal)}
.service p{font-size:12px;color:var(--muted);margin-top:6px;line-height:17px}

/* welcome */
.welcome{top:928px;height:432px;background:var(--light)}
.welcome-text{position:absolute;left:0;top:52px;width:480px}
.welcome-text h2{font-family:"Roboto",sans-serif;font-size:30px;font-weight:400;color:var(--charcoal)}
.welcome-text h2 small{font-size:12px;color:var(--orange);font-weight:500;margin-left:6px}
.welcome-text p{font-size:13px;line-height:20px;color:var(--muted);margin-top:18px}
.features{display:flex;gap:60px;margin-top:28px}
.feature{width:100px;text-align:center;font-size:12px;line-height:16px;color:var(--ink)}
.feature .ico{width:48px;height:48px;border-radius:50%;background:var(--white);margin:0 auto 8px;display:flex;align-items:center;justify-content:center}
.welcome-media{position:absolute;right:0;top:44px;width:460px;height:328px;border:6px solid var(--orange);background:linear-gradient(180deg,#9fb0bf,#4d5a66)}
.play{position:absolute;left:50%;top:50%;width:56px;height:56px;margin:-28px 0 0 -28px;border-radius:50%;background:rgba(255,255,255,.85)}
.play::after{content:"";position:absolute;left:22px;top:17px;border-left:16px solid var(--charcoal);border-top:11px solid transparent;border-bottom:11px solid transparent}
.media-nav{position:absolute;right:8px;bottom:8px;display:flex;gap:4px}
.media-nav span{width:18px;height:18px;background:var(--white)}

/* testimonials */
.testimonials{top:1360px;height:252px;background:var(--white);text-align:center}
.testimonials .sec-title{padding-top:20px;font-size:28px}
.testimonials .sec-sub{margin-top:4px;font-size:13px}
.quotes{display:flex;justify-content:space-between;margin-top:28px;text-align:left}
.quote{width:500px;display:flex;gap:20px}
.avatar{width:110px;flex:none;text-align:center;font-size:12px;color:var(--muted)}
.avatar .photo{width:100px;height:100px;margin:0 auto 8px;background:linear-gradient(180deg,#c9ced3,#7f8891);border-radius:50%}
.quote p{font-size:13px;line-height:19px;color:var(--muted);border-left:3px solid var(--orange);padding-left:14px;font-style:italic}
.dots{display:flex;justify-content:center;gap:6px;margin-top:18px}
.dots span{width:20px;height:20px;background:var(--line)}
.dots span.on{background:var(--orange)}

/* cta band */
.band{top:1612px;height:116px;background:var(--orange)}
.band-text{position:absolute;left:0;top:28px;width:640px;color:var(--white);font-weight:700;font-size:20px;line-height:30px}
.call-box{position:absolute;right:0;top:18px;width:250px;height:80px;background:var(--orange-dark);color:var(--white);text-align:center;padding-top:12px}
.call-box span{font-size:14px}
.call-box strong{display:block;font-size:26px;font-weight:700;margin-top:2px}

/* footer */
.contact{top:1728px;height:424px}
.map{position:absolute;inset:0;background:linear-gradient(135deg,#d9dcd8,#c5cbc6 50%,#d4d7d2)}
.contact-info{position:absolute;left:0;top:34px;width:340px;background:rgba(255,255,255,.88);padding:20px}
.contact-info h4{font-size:15px;font-weight:700;color:var(--charcoal);margin-bottom:12px}
.info-row{display:flex;gap:10px;margin-bottom:12px;font-size:12px;line-height:16px;color:var(--ink)}
.info-row .ic{width:22px;height:22px;flex:none;border-radius:50%;background:var(--orange)}
.footer-brand{position:absolute;left:400px;top:130px;width:260px;text-align:center;display:flex;align-items:center;justify-content:center;gap:12px}
.footer-brand .dot{width:60px;height:60px;border-radius:50%;background:var(--orange);opacity:.75}
.footer-brand span{font-family:"Roboto",sans-serif;font-weight:700;font-size:34px;color:var(--charcoal);opacity:.6}
.request{position:absolute;right:0;top:34px;width:340px;background:var(--navy);padding:18px 22px;color:var(--white)}
.request h4{font-size:18px;font-weight:700;text-transform:uppercase;display:flex;align-items:center;gap:10px}
.request h4 i{width:30px;height:30px;border-radius:50%;background:var(--orange)}
.request p{font-size:12px;color:#bbbbbb;margin:8px 0 12px}
.field{height:30px;background:var(--white);margin-bottom:8px;font-size:12px;color:#999;padding:7px 10px}
.field.tall{height:66px}
.request .btn{font-size:13px;padding:8px 20px}

.bottom-bar{top:2152px;height:52px;background:var(--charcoal);color:#aaaaaa;font-size:12px;text-align:center;line-height:52px}
</style>
</head>
<body>

<header class="hero">
  <div class="hero-photo" role="img" aria-label="Stock photo of a high-rise building under construction with cranes"></div>
  <div class="topbar">
    <div class="brand"><span class="brand-dot"></span><span class="brand-name">TALVERO</span></div>
    <nav class="nav"><span>About</span><span>About Us</span><span>Services</span><span>Testimonials</span><span>Contact Us</span><span class="phone">123 456 7890</span></nav>
  </div>
  <span class="slide-arrow left"></span><span class="slide-arrow right"></span>
  <p class="hero-text">Lorem ipsum dolor sit amet consectetur adipisicing elitsed do eiusmod tempor<br>incididunt ut labore dolo magna aliqua.</p>
  <div class="hero-cta"><span class="btn">Get Started With Us</span></div>
</header>

<section class="services">
  <div class="wrap">
    <h2 class="sec-title">OUR <b>SERVICES</b></h2>
    <p class="sec-sub">Lorem ipsum dolor sit amet, consectetur adipiscing elit. Aenean et dignissim sem. Interdum risus. Vestibulum consectetur.</p>
    <div class="service-grid">
      <div class="service"><div class="ring"><svg width="38" height="38" viewBox="0 0 38 38" fill="none" stroke="#333" stroke-width="2.5"><path d="M6 26h26M9 26a10 10 0 0 1 20 0M19 12v-4"/></svg></div><h3>Civil Engineering</h3><p>Lorem ipsum dolor sit<br>amet adipiscing elit</p></div>
      <div class="service"><div class="ring"><svg width="38" height="38" viewBox="0 0 38 38" fill="none" stroke="#333" stroke-width="2.5"><rect x="8" y="8" width="10" height="24"/><rect x="20" y="16" width="10" height="16"/></svg></div><h3>Structural Engineering</h3><p>Lorem ipsum dolor sit<br>amet adipiscing elit</p></div>
      <div class="service"><div class="ring"><svg width="38" height="38" viewBox="0 0 38 38" fill="none" stroke="#333" stroke-width="3"><circle cx="19" cy="19" r="12"/><path d="M13 19l4 4 8-8"/></svg></div><h3>Project Management</h3><p>Lorem ipsum dolor sit<br>amet adipiscing elit</p></div>
      <div class="service"><div class="ring"><svg width="38" height="38" viewBox="0 0 38 38" fill="none" stroke="#333" stroke-width="2.5"><path d="M7 30h24M10 30V20M17 30V14M24 30V18M31 30V9"/></svg></div><h3>Business Management</h3><p>Lorem ipsum dolor sit<br>amet adipiscing elit</p></div>
      <div class="service"><div class="ring"><svg width="38" height="38" viewBox="0 0 38 38" fill="none" stroke="#333" stroke-width="2.5"><circle cx="19" cy="19" r="5"/><path d="M19 5v6M19 27v6M5 19h6M27 19h6"/></svg></div><h3>Project Controls</h3><p>Lorem ipsum dolor sit<br>amet adipiscing elit</p></div>
      <div class="service"><div class="ring"><svg width="38" height="38" viewBox="0 0 38 38" fill="none" stroke="#333" stroke-width="2.5"><path d="M19 6l-9 26M19 6l9 26M13 24h12"/></svg></div><h3>Project Drafting</h3><p>Lorem ipsum dolor sit<br>amet adipiscing elit</p></div>
    </div>
  </div>
</section>

<section class="welcome">
  <div class="wrap">
    <div class="welcome-text">
      <h2>Welcome to Talvero<small>Engineering &amp; Management Services</small></h2>
      <p>Lorem ipsum dolor sit amet, consectetuer adipiscing elit, sed diam nonummy nibh euismod tincidunt ut laoreet dolore magna aliquam erat volutpat. Ut wisi enim ad minim veniam, quis nostrud exerci tation ullamcorper suscipit lobortis nisl ut aliquip ex ea commodo consequat.</p>
      <p>Duis autem vel eum iriure dolor in hendrerit in vulputate velit esse molestie consequat, vel illum dolore eu feugiat nulla facilisis at vero eros et accumsan et iusto odio dignissim qui blandit praesent luptatum zzril delenit augue duis.</p>
      <div class="features">
        <div class="feature"><div class="ico"><svg width="24" height="24" viewBox="0 0 24 24" fill="none" stroke="#f15a22" stroke-width="2.5"><circle cx="12" cy="12" r="8"/><path d="M12 7v10"/></svg></div>Value for<br>Money</div>
        <div class="feature"><div class="ico"><svg width="24" height="24" viewBox="0 0 24 24" fill="none" stroke="#f15a22" stroke-width="2.5"><path d="M5 19L19 5M8 5l11 11"/></svg></div>Professional<br>Design Ideas</div>
        <div class="feature"><div class="ico"><svg width="24" height="24" viewBox="0 0 24 24" fill="none" stroke="#f15a22" stroke-width="2.5"><path d="M5 12l5 5 9-10"/></svg></div>Quality<br>Guaranteed 100%</div>
      </div>
    </div>
    <div class="welcome-media" role="img" aria-label="Video still of a large steel-framed industrial hall interior">
      <span class="play"></span>
      <div class="media-nav"><span></span><span></span></div>
    </div>
  </div>
</section>

<section class="testimonials">
  <div class="wrap">
    <h2 class="sec-title">Client Testimonials</h2>
    <p class="sec-sub">See What Our Say About us</p>
    <div class="quotes">
      <div class="quote"><div class="avatar"><div class="photo" role="img" aria-label="Portrait photo of a client"></div>Lorem ipsum</div><p>Lorem ipsum dolor sit amet consectetuer adipiscing elitsed do eiusmod tempor incididunt ut labore dolor magna aliqua. Ut enim ad minim veniam, quis nostrud exercitation ullamco laboris nisi ut aliquip ex ea commodo consequat.</p></div>
      <div class="quote"><div class="avatar"><div class="photo" role="img" aria-label="Portrait photo of a client"></div>Lorem ipsum</div><p>Lorem ipsum dolor sit amet consectetuer adipiscing elitsed do eiusmod tempor incididunt ut labore dolor magna aliqua. Ut enim ad minim veniam, quis nostrud exercitation ullamco laboris nisi ut aliquip ex ea commodo consequat.</p></div>
    </div>
    <div class="dots"><span></span><span class="on"></span></div>
  </div>
</section>

<section class="band">
  <div class="wrap">
    <p class="band-text">Lorem ipsum dolor sit amet consectetur adipisicing elitsed do eiusmod tempor incididunt ut labore dolo magna aliqua.</p>
    <div class="call-box"><span>Call Us Today</span><strong>123 456 7890</strong></div>
  </div>
</section>

<section class="contact">
  <div class="map" role="img" aria-label="Street map showing the office location"></div>
  <div class="wrap">
    <div class="contact-info">
      <h4>Contact Information</h4>
      <div class="info-row"><span class="ic"></span><div>Postal Address<br>Harbourline Road 14, 2040 Northvale</div></div>
      <div class="info-row"><span class="ic"></span><div>Telephone<br>123-456-7890</div></div>
      <div class="info-row"><span class="ic"></span><div>Email<br>Information and Support: hello@talveroeng.com</div></div>
      <div class="info-row"><span class="ic"></span><div>Social<br>www.social.example/talveroeng</div></div>
      <div class="info-row"><span class="ic"></span><div>Photos<br>www.photos.example/talveroeng</div></div>
    </div>
    <div class="footer-brand"><span class="dot"></span><span>TALVERO</span></div>
    <div class="request">
      <h4><i></i>Send Request</h4>
      <p>Lorem ipsum dolor sit amet, consectetur.</p>
      <div class="field">Name</div>
      <div class="field">Email</div>
      <div class="field">Phone</div>
      <div class="field tall">Message</div>
      <span class="btn">Submit</span>
    </div>
  </div>
</section>

<footer class="bottom-bar">© 2016 Talvero Engineering &amp; Management Services. All rights reserved.</footer>

</body>
</html>
```